We need a business card design for an Afghan catering business called 'Velmi Catering'. We provide Afghan food for any occasions such as wedding, birthday, engagement, small gathering, etc. We would like the business card to include the name of the business designed with the logo, phone number, and the address. We already have our logo that we would upload. The design that we require or suggest must be black with the logo and if possible change the colors of the logo (e.g. the logo includes red and gray lines) to gold. In other words, we would like the business card color to be black with some luxury design that would match the logo. For the front, we would like the logo which includes the name of the business, contact info, and the address. Also, depending on the design we would like to include some pictures of the food. the location (map), facebook, and instagram. After having a look at the design of the business card, we also need menu design and flyer design same thing as the business card design.

Industry/Entity Type

Business

Contact Information for Business Card

Title: Velmi Catering
Phone #: 5550142863 and 5550197214
Name: Lutfiya

Font styles to use
Serif
Script

Colors
000000

Requirements
Must have
• My project must have the name (with the logo), phone number, email, name, address, map, a few picture of the food, facebook, and Instagram logo.
Nice to have
• The color and font must match the logo. It must look simple and luxury (with suggested color black).

```html
<!DOCTYPE html>
<html lang="en">
<head>
<meta charset="utf-8">
<title>Velmi Catering – Business Card</title>
<link rel="stylesheet" href="https://fonts.googleapis.com/css2?family=Montserrat:wght@300;500;600&display=swap">
<style>
  :root {
    --page: #ffffff;
    --black: #000000;
    --gold: #c9a13a;
    --gold-light: #f7eeb0;
    --gold-deep: #8a5e1e;
    --text-muted: #b99a52;
  }
  * { margin: 0; padding: 0; box-sizing: border-box; }
  html, body { width: 1200px; height: 1000px; overflow: hidden; background: var(--page); }
  body { position: relative; font-family: "Montserrat", Arial, sans-serif; }

  .card { position: absolute; left: 263px; width: 675px; height: 396px; overflow: hidden; }
  .card-front { top: 82px; }
  .card-back { top: 522px; background: var(--black); }
  .card svg { position: absolute; inset: 0; display: block; }

  .brand-name {
    position: absolute;
    color: var(--gold);
    font-weight: 600;
    text-align: center;
    line-height: 1.1;
  }
  .card-front .brand-name { left: 240px; top: 170px; width: 200px; font-size: 27px; }
  .card-back .brand-name { left: 40px; top: 52px; width: 210px; font-size: 28px; text-align: left; }

  .person-name {
    position: absolute; left: 57px; top: 174px;
    color: var(--gold); font-weight: 500; font-size: 40px;
  }
  .contact-list {
    position: absolute; left: 57px; top: 250px;
    list-style: none; color: var(--text-muted);
    font-weight: 300; font-size: 14.5px; line-height: 19px;
  }
  .contact-list .gap { height: 19px; }
</style>
</head>
<body>

<section class="card card-front" aria-label="Card front">
  <svg viewBox="0 0 675 396" width="675" height="396">
    <defs>
      <linearGradient id="goldSheen" x1="0" y1="1" x2="1" y2="0">
        <stop offset="0" stop-color="#9a6a22"/>
        <stop offset="0.18" stop-color="#d9b55a"/>
        <stop offset="0.42" stop-color="#fbf3bf"/>
        <stop offset="0.62" stop-color="#f2df96"/>
        <stop offset="0.8" stop-color="#e2ac35"/>
        <stop offset="1" stop-color="#8a5e1e"/>
      </linearGradient>
      <linearGradient id="goldEdge" x1="0" y1="0" x2="1" y2="1">
        <stop offset="0" stop-color="#f7eeb0"/>
        <stop offset="1" stop-color="#a9762a"/>
      </linearGradient>
    </defs>
    <rect width="675" height="396" fill="url(#goldSheen)"/>
    <rect y="150" width="675" height="95" fill="#000"/>
    <line x1="0" y1="150" x2="675" y2="150" stroke="url(#goldEdge)" stroke-width="2"/>
    <line x1="0" y1="245" x2="675" y2="245" stroke="url(#goldEdge)" stroke-width="2"/>
    <circle cx="340" cy="210" r="112" fill="#000" stroke="url(#goldEdge)" stroke-width="3"/>
  </svg>
  <div class="brand-name">Velmi<br>Catering</div>
</section>

<section class="card card-back" aria-label="Card back">
  <svg viewBox="0 0 675 396" width="675" height="396">
    <defs>
      <linearGradient id="ringGold" x1="0" y1="0" x2="0" y2="1">
        <stop offset="0" stop-color="#8a5e1e"/>
        <stop offset="0.45" stop-color="#f7eeb0"/>
        <stop offset="1" stop-color="#b8862e"/>
      </linearGradient>
      <linearGradient id="ruleGold" x1="0" y1="0" x2="1" y2="0">
        <stop offset="0" stop-color="#8a5e1e"/>
        <stop offset="0.5" stop-color="#f2d98a"/>
        <stop offset="1" stop-color="#8a5e1e"/>
      </linearGradient>
      <linearGradient id="foodTones" x1="0" y1="0" x2="0.6" y2="1">
        <stop offset="0" stop-color="#e9dcc4"/>
        <stop offset="0.35" stop-color="#d8c7a8"/>
        <stop offset="0.55" stop-color="#e0662a"/>
        <stop offset="0.75" stop-color="#3a2418"/>
        <stop offset="1" stop-color="#d85a20"/>
      </linearGradient>
    </defs>
    <line x1="0" y1="230" x2="376" y2="230" stroke="url(#ruleGold)" stroke-width="3"/>
    <circle cx="625" cy="200" r="248" fill="url(#ringGold)"/>
    <circle cx="625" cy="200" r="236" fill="url(#foodTones)" role="img"
            aria-label="Photo of Afghan rice dish topped with carrots and raisins"/>
  </svg>
  <div class="brand-name">Velmi<br>Catering</div>
  <div class="person-name">Lutfiya</div>
  <ul class="contact-list">
    <li>Lutfiya - Cell: 555 014 2863</li>
    <li>Soraya - Cell: 555 019 7214</li>
    <li>email: hello@velmicatering.com</li>
    <li class="gap"></li>
    <li>facebook: Velmi Catering - Lutfiya</li>
    <li>Instagram: @velmicatering</li>
  </ul>
</section>

</body>
</html>
```